Exercise Physiologist needs business cards

I have a logo, I need business cards (Sole trader) as I am moving to a new location and would like an updated look. I provide gym based exercise rehabilitation, injury prevention and movement assessments. I have over 13 years experience as an Exercise Physiologist. I would like the cards to look professional but not boring and can be a little different to stand out when sitting with other Allied Health Professional cards.

Target Market(s)

GP's, Allied health practitioners, people with injuries wanting to exercise

Industry/Entity Type

Health And Wellness

Contact Information for Business Card

Megan Dorrit - Exercise Physiologist 0437 582 906
14 Larkspur Bend Rd
South Geelong
(Gate 2, Brannock Fitness)
vantorahealth@maildrop-example.com
socialpage-example.com/Vantora

Requirements
Must have
• I would like to include a section to add next appointment date and time space to the back of the card.
Nice to have
• Rounded corners and a black background on 1 or 2 sides.
Should not have
• Pictures of fit/toned bodies etc

```html
<!DOCTYPE html>
<html lang="en">
<head>
<meta charset="utf-8">
<title>Megan Dorrit – Business Cards</title>
<link href="https://fonts.googleapis.com/css2?family=Montserrat:wght@400;500;700&display=swap" rel="stylesheet">
<style>
  :root {
    --bg: #262626;
    --card: #1d1d1d;
    --blue-deep: #2f5fae;
    --blue-mid: #3d67b0;
    --blue-light: #6fa6d8;
    --blue-soft: #4a9bd1;
    --muted: #8a9ec0;
    --rule: #3a4d6e;
  }
  html, body {
    margin: 0;
    padding: 0;
    width: 1200px;
    height: 900px;
    overflow: hidden;
    background: var(--bg);
    font-family: "Montserrat", sans-serif;
  }
  .canvas {
    position: relative;
    width: 1200px;
    height: 900px;
  }
  .card {
    position: absolute;
    top: 166px;
    width: 324px;
    height: 568px;
    background: var(--card);
    border-radius: 3px;
    text-align: center;
  }
  .card--front { left: 262px; }
  .card--back { left: 612px; }

  .person {
    position: absolute;
    top: 78px;
    left: 0;
    right: 0;
  }
  .person__name {
    margin: 0;
    font-size: 21px;
    font-weight: 700;
    letter-spacing: 1.5px;
    color: var(--blue-deep);
    text-transform: uppercase;
    line-height: 1.2;
  }
  .person__role {
    margin: 2px 0 0;
    font-size: 13.5px;
    font-weight: 500;
    letter-spacing: 1.2px;
    color: var(--blue-light);
    text-transform: uppercase;
  }
  .divider {
    display: block;
    width: 18px;
    height: 2px;
    margin: 10px auto 0;
    background: var(--blue-soft);
  }

  .brand {
    position: absolute;
    left: 0;
    right: 0;
  }
  .card--front .brand { top: 190px; }
  .card--back .brand { top: 150px; }
  .brand__dot {
    display: block;
    width: 68px;
    height: 68px;
    margin: 0 auto;
    border-radius: 50%;
    background: var(--blue-soft);
  }
  .brand__name {
    margin: 14px 0 0;
    font-size: 40px;
    font-weight: 500;
    color: var(--blue-deep);
    line-height: 1;
  }

  .contact {
    position: absolute;
    top: 400px;
    left: 0;
    right: 0;
    font-size: 13px;
    line-height: 18px;
    color: var(--blue-mid);
  }
  .contact__address {
    margin: 0;
    font-style: normal;
  }
  .contact__note { color: var(--muted); }
  .contact__phone { margin: 11px 0 0; }
  .contact__online {
    margin: 8px 0 0;
    font-size: 11.5px;
    line-height: 17px;
    color: var(--muted);
  }

  .appointment {
    position: absolute;
    top: 350px;
    left: 42px;
    right: 42px;
    text-align: left;
  }
  .appointment__title {
    margin: 0 0 18px;
    font-size: 12.5px;
    font-weight: 700;
    letter-spacing: 1.5px;
    color: var(--blue-light);
    text-transform: uppercase;
    text-align: center;
  }
  .appointment__field {
    display: flex;
    align-items: flex-end;
    gap: 10px;
    margin: 0 0 22px;
    font-size: 12px;
    font-weight: 500;
    letter-spacing: 1px;
    color: var(--blue-mid);
    text-transform: uppercase;
  }
  .appointment__line {
    flex: 1;
    height: 1px;
    margin-bottom: 3px;
    background: var(--rule);
  }
</style>
</head>
<body>
<main class="canvas">
  <section class="card card--front" aria-label="Card front">
    <header class="person">
      <h1 class="person__name">Megan Dorrit</h1>
      <p class="person__role">Exercise Physiologist</p>
      <span class="divider"></span>
    </header>
    <div class="brand">
      <span class="brand__dot"></span>
      <p class="brand__name">Vantora</p>
    </div>
    <div class="contact">
      <address class="contact__address">
        14 Larkspur Bend Rd<br>
        South Geelong<br>
        <span class="contact__note">(Gate 2, Brannock Fitness)</span>
      </address>
      <p class="contact__phone">0437 582 906</p>
      <p class="contact__online">
        vantorahealth@maildrop-example.com<br>
        socialpage-example.com/Vantora
      </p>
      <span class="divider"></span>
    </div>
  </section>

  <section class="card card--back" aria-label="Card back">
    <div class="brand">
      <span class="brand__dot"></span>
      <p class="brand__name">Vantora</p>
    </div>
    <div class="appointment">
      <p class="appointment__title">Next Appointment</p>
      <div class="appointment__field"><span>Date</span><span class="appointment__line"></span></div>
      <div class="appointment__field"><span>Time</span><span class="appointment__line"></span></div>
    </div>
  </section>
</main>
</body>
</html>
```